quorVale - website to pay membership association fee

The main purpose of this site it to allow a pre-registered user to be able to view the membership fees for their membership association and pay the same in one of the ways offered by the portal.
You are required to create a graphical project only for the logon functions as a user, while omitting the back end/administration ones that will be decided later
The site, besides being responsive must be very intuitive in its function. The graphics must be bright.

Number of Pages Required

4 page

Requirements
Must have
• i need to see template for
• 1. Home page
• 2. Page after login. People can se one or more bill to Pay and decide to see more details or to pay.
• 3. Page to Pay. Choose the desired payment method five alternative

```html
<!DOCTYPE html>
<html lang="en">
<head>
<meta charset="utf-8">
<title>quorVale – Payment</title>
<link rel="stylesheet" href="https://fonts.googleapis.com/css2?family=Roboto+Condensed:wght@400&family=Roboto:wght@300;400;500&display=swap">
<style>
  :root {
    --ink: #3b4658;
    --ink-soft: #6d7785;
    --placeholder: #8e97a4;
    --field-bg: #eceef2;
    --field-border: #d3d8e0;
    --rule: #cfd6df;
    --brand: #0b7bd3;
    --brand-dark: #0a6fc0;
    --success: #1dbf57;
    --white: #ffffff;
  }
  * { box-sizing: border-box; margin: 0; padding: 0; }
  html, body { width: 1200px; height: 3000px; overflow: hidden; background: var(--white); }
  body { position: relative; font-family: "Roboto", sans-serif; font-weight: 300; color: var(--ink); }

  .abs { position: absolute; }

  .close-btn { left: 868px; top: 60px; width: 32px; height: 32px; }

  .section-title {
    font-family: "Roboto Condensed", sans-serif; font-weight: 400;
    font-size: 37px; color: var(--ink); letter-spacing: 0.5px;
    left: 192px; line-height: 40px;
  }
  .rule { left: 134px; width: 738px; height: 2px; background: var(--rule); }
  .rule-v { width: 2px; background: var(--rule); }

  .field {
    left: 194px; width: 620px; height: 88px;
    background: var(--field-bg); border: 2px solid var(--field-border); border-radius: 8px;
    padding-left: 30px; display: flex; align-items: center;
    font-size: 30px; color: var(--placeholder);
  }
  .field.center { padding-left: 0; justify-content: center; }

  .radio {
    width: 48px; height: 48px; border-radius: 50%;
    background: var(--field-bg); border: 2px solid var(--field-border);
    display: flex; align-items: center; justify-content: center;
  }
  .radio.is-checked::after {
    content: ""; width: 14px; height: 14px; border-radius: 50%; background: #7f8896;
  }

  .method-cell { width: 370px; text-align: center; }
  .method-label { font-size: 30px; color: var(--ink-soft); line-height: 40px; }
  .method-label strong { font-weight: 400; color: var(--ink); }

  .brand-name {
    font-family: "Roboto", sans-serif; font-weight: 500; font-size: 28px; color: var(--brand);
    display: flex; align-items: center; gap: 12px; white-space: nowrap;
  }
  .brand-dot { width: 20px; height: 20px; border-radius: 50%; background: var(--brand); }
  .brand-square { width: 18px; height: 18px; background: var(--brand); }

  .wire-label {
    left: 240px; top: 752px; width: 152px; height: 94px;
    border: 2px solid #58b9e6; border-radius: 6px;
    display: flex; align-items: center; justify-content: center;
    font-weight: 500; font-size: 24px; line-height: 26px; color: var(--brand); text-align: center;
  }

  .option-row { display: flex; align-items: center; gap: 18px; font-size: 30px; color: var(--ink-soft); }

  .total { font-size: 33px; color: var(--ink-soft); line-height: 40px; }
  .total b { font-weight: 400; color: var(--ink); }

  .back-btn {
    width: 80px; height: 80px; border: 2px solid var(--field-border); border-radius: 6px;
    display: flex; align-items: center; justify-content: center; background: var(--white);
  }
  .primary-btn {
    background: var(--brand); color: var(--white); border-radius: 6px;
    font-weight: 500; font-size: 28px; letter-spacing: 0.5px;
    display: flex; align-items: center; justify-content: center; gap: 16px;
  }

  .checkbox {
    left: 194px; top: 1808px; width: 50px; height: 50px; border-radius: 6px;
    background: var(--field-bg); border: 2px solid var(--field-border);
    display: flex; align-items: center; justify-content: center;
  }
  .check-text { left: 262px; top: 1812px; font-size: 30px; color: var(--ink-soft); line-height: 40px; }

  .success-icon { left: 462px; top: 2276px; width: 76px; height: 76px; }
  .thanks-title {
    left: 0; width: 1004px; top: 2388px; text-align: center;
    font-family: "Roboto Condensed", sans-serif; font-size: 40px; color: var(--ink);
  }
  .thanks-text {
    left: 0; width: 1004px; top: 2462px; text-align: center;
    font-size: 30px; line-height: 52px; color: var(--ink-soft);
  }
</style>
</head>
<body>

  <!-- Step 1: payment details -->
  <svg class="abs close-btn" viewBox="0 0 32 32" aria-label="Close">
    <path d="M5 5 L27 27 M27 5 L5 27" stroke="#8a94a3" stroke-width="3" stroke-linecap="round"/>
  </svg>

  <h1 class="abs section-title" style="top:100px;">PAYMENT DETAILS</h1>
  <div class="abs rule" style="top:190px;"></div>

  <div class="abs field" style="top:252px;">Your Full Name</div>
  <div class="abs field" style="top:382px;">Email Address</div>

  <div class="abs rule" style="top:490px;"></div>
  <div class="abs rule-v" style="left:503px; top:490px; height:504px;"></div>
  <div class="abs rule" style="top:744px;"></div>
  <div class="abs rule" style="top:994px;"></div>

  <!-- card option -->
  <div class="abs brand-name" style="left:200px; top:512px; gap:22px; font-size:24px;">
    <span>Varno</span><span>Meridia</span><span>Corvex</span>
  </div>
  <div class="abs radio is-checked" style="left:294px; top:590px;"></div>
  <div class="abs method-cell method-label" style="left:134px; top:668px;">Pay with <strong>Credit Card</strong></div>

  <!-- wallet option -->
  <div class="abs brand-name" style="left:604px; top:510px; font-size:34px;">
    <span class="brand-dot"></span><span>Penvo</span>
  </div>
  <div class="abs radio" style="left:664px; top:590px;"></div>
  <div class="abs method-cell method-label" style="left:504px; top:668px;">Pay with <strong>Penvo</strong></div>

  <!-- wire option -->
  <div class="abs wire-label">WIRE<br>TRANSFER</div>
  <div class="abs radio" style="left:290px; top:854px;"></div>
  <div class="abs method-cell method-label" style="left:130px; top:930px;">Pay via Wire Transfer</div>

  <!-- other options -->
  <div class="abs option-row" style="left:546px; top:774px;"><span class="radio"></span>Pay in Installment</div>
  <div class="abs option-row" style="left:546px; top:858px;"><span class="radio"></span>Preferred Payment</div>

  <div class="abs total" style="left:192px; top:1054px;">Total: <b>$107</b></div>
  <div class="abs back-btn" style="left:463px; top:1036px;">
    <svg width="34" height="24" viewBox="0 0 34 24"><path d="M32 12 H3 M13 2 L3 12 L13 22" fill="none" stroke="#a9b1bd" stroke-width="2.5" stroke-linecap="round" stroke-linejoin="round"/></svg>
  </div>
  <div class="abs primary-btn" style="left:564px; top:1036px; width:250px; height:80px;">
    CONTINUE
    <svg width="34" height="26" viewBox="0 0 34 26"><path d="M2 13 H31 M20 2 L31 13 L20 24" fill="none" stroke="#fff" stroke-width="3.5" stroke-linecap="round" stroke-linejoin="round"/></svg>
  </div>

  <svg class="abs" style="left:896px; top:1146px;" width="120" height="154" viewBox="0 0 120 154" aria-hidden="true">
    <path d="M42 0 H78 V86 H120 L60 154 L0 86 H42 Z" fill="var(--brand)"/>
  </svg>

  <!-- Step 2: card payment -->
  <h2 class="abs section-title" style="top:1264px;">PAYMENT</h2>
  <div class="abs rule" style="top:1356px;"></div>

  <div class="abs field" style="top:1418px;">Card Number</div>
  <div class="abs field" style="top:1548px;">Name on Card</div>
  <div class="abs field center" style="top:1678px; width:174px;">CV Code</div>
  <div class="abs total" style="left:454px; top:1702px; font-size:30px;">Expiry Date:</div>
  <div class="abs field center" style="top:1678px; left:638px; width:176px;">MM / YY</div>

  <div class="abs checkbox">
    <svg width="28" height="22" viewBox="0 0 28 22"><path d="M3 11 L11 19 L25 3" fill="none" stroke="#7c8ea6" stroke-width="3" stroke-linecap="round" stroke-linejoin="round"/></svg>
  </div>
  <div class="abs check-text">Save info for future purchases</div>

  <div class="abs rule" style="top:1918px;"></div>

  <div class="abs total" style="left:192px; top:1978px;">Total: <b>$107</b></div>
  <div class="abs back-btn" style="left:463px; top:1960px;">
    <svg width="34" height="24" viewBox="0 0 34 24"><path d="M32 12 H3 M13 2 L3 12 L13 22" fill="none" stroke="#a9b1bd" stroke-width="2.5" stroke-linecap="round" stroke-linejoin="round"/></svg>
  </div>
  <div class="abs primary-btn" style="left:564px; top:1960px; width:250px; height:80px;">
    CONTINUE
    <svg width="34" height="26" viewBox="0 0 34 26"><path d="M2 13 H31 M20 2 L31 13 L20 24" fill="none" stroke="#fff" stroke-width="3.5" stroke-linecap="round" stroke-linejoin="round"/></svg>
  </div>

  <svg class="abs" style="left:874px; top:2284px;" width="116" height="152" viewBox="0 0 116 152" aria-hidden="true">
    <path d="M40 0 H76 V86 H116 L58 152 L0 86 H40 Z" fill="var(--brand)"/>
  </svg>

  <!-- Step 3: confirmation -->
  <svg class="abs success-icon" viewBox="0 0 76 76" aria-hidden="true">
    <circle cx="38" cy="38" r="38" fill="var(--success)"/>
    <path d="M25 39 L34 48 L52 29" fill="none" stroke="#fff" stroke-width="4" stroke-linecap="round" stroke-linejoin="round"/>
  </svg>
  <h2 class="abs thanks-title">THANK YOU!</h2>
  <p class="abs thanks-text">Your payment shall be processed by our<br>payment provider,</p>
  <div class="abs primary-btn" style="left:390px; top:2594px; width:226px; height:78px;">HOME</div>

</body>
</html>
```